Auction Company Wordpress Design Project

We need a WordPress design/concept for an established auctioneering company specializing in Benefit Auctions, Estate Auctions, Business Liquidations/Overstocks, and real estate marketing in the Chicago area. The winning design will have a professional look appealing to clients searching for these services.

Industry/Entity Type

Real Estate

Requirements
Must have
• - We will require winning designer to provide a layered PSD (Adobe photoshop) concept file, along with any non-standard font files used.

The site's navigation: 1) Home, 2) Auctions, 3) About Us, 4) Buyers, 5) Sellers, 6) Media, 7) Contact Us. Horizontal structure preferred.

A slideshow element will be represented (choice of files attached) preferably in the header. The following widgets will also be incorporated into sidebar (or other creative placement):
- Brightway Mailer email signup
- Featured Auctions (example shown in http://www.bidlantern-example.com/ as "Upcoming Auctions" widget)
- Vidora video widget
- Social media widget for Friendlyn, Chirpel, Vidora icons
- Testimonials widget

Winning design will creatively use colors in logo (with perhaps accent color) with a professional, clean look. Client mentions liking the use of color in http://www.plotgleam-example.com/

Footer of site will have generic contact info (phone number, email addresses, mailing address; a smaller instance of logo; and the attached association logos.
Nice to have
• - Use of drop-down menus should be demonstrated by incorporating mouse-over for 1) Upcoming, 2) Online, 3) Past, under the 'Auctions' main menu item (for clarity of design, this drop-down can be placed under any other menu item if necessary).
Should not have
• Please do not use auction gavels in the design.

```html
<!DOCTYPE html>
<html lang="en">
<head>
<meta charset="utf-8">
<title>Harborline Auction Realty</title>
<link href="https://fonts.googleapis.com/css2?family=Cabin:wght@400;500;600&family=Arimo:wght@400;700&display=swap" rel="stylesheet">
<style>
:root{
  --ink:#222;
  --body:#333;
  --dark:#2b3039;
  --darker:#1a1a1a;
  --gold-hi:#e2d5b0;
  --gold-lo:#b9a577;
  --gold-text:#b89a3f;
  --rust:#b0501a;
  --cream:#ece8cf;
  --rule:#ddd;
  --white:#fff;
}
*{box-sizing:border-box;margin:0;padding:0}
html,body{width:1083px;height:1200px;overflow:hidden}
body{position:relative;background:var(--white);font-family:Arimo,Arial,sans-serif;color:var(--body)}
.abs{position:absolute}
.photo{display:block}

/* header */
.topline{left:0;top:0;width:1083px;height:5px;background:var(--dark)}
.header{left:0;top:5px;width:1083px;height:141px;background:linear-gradient(#f6f6f6,#fff)}
.brand{left:134px;top:26px;width:130px;font-family:Cabin,sans-serif;font-weight:600;color:#3a3a3a;font-size:25px;line-height:24px;text-transform:uppercase;text-align:center}
.brand small{display:block;font-size:14px;line-height:17px;letter-spacing:.5px}
.mailer-label{left:698px;top:24px;font:bold 12px Arimo,sans-serif;color:var(--ink)}
.mailer-input{left:808px;top:18px;width:176px;height:24px;border:1px solid #ccc;background:#fff;font-size:11px;color:#999;padding:5px 6px}
.join{left:912px;top:51px;width:70px;height:25px;background:linear-gradient(#444,#111);color:#fff;font:bold 11px Arimo,sans-serif;text-align:center;line-height:25px}
.follow{left:404px;top:99px;font:500 16px Cabin,sans-serif;color:var(--ink)}
.social{left:502px;top:94px;display:flex;gap:5px}
.social span{width:27px;height:27px;border-radius:50%;background:#222}
.phone{left:793px;top:97px;display:flex;align-items:center;gap:12px;font:400 18px Cabin,sans-serif;color:#555}

/* nav */
.nav{left:0;top:146px;width:1083px;height:49px;background:linear-gradient(var(--dark) 0 6px,var(--gold-hi) 6px,var(--gold-lo));display:flex}
.nav a{display:flex;align-items:center;justify-content:center;height:43px;margin-top:6px;font:500 12.5px Cabin,sans-serif;color:var(--darker);text-decoration:none;border-right:1px solid #8a7c58}
.nav a:last-child{border-right:0}
.dropdown{left:329px;top:195px;width:136px;background:var(--cream);z-index:3}
.dropdown div{height:30px;line-height:30px;padding-left:12px;font:500 12.5px Cabin,sans-serif;color:var(--ink)}
.dropdown div::before{content:"» ";font-size:10px}
.dropdown .on{background:#77746b;color:#fff;height:34px;line-height:34px}

/* hero */
.hero{left:0;top:195px;width:1083px;height:351px;background:var(--dark)}
.featured{left:100px;top:210px;width:253px;height:325px;background:linear-gradient(#e4d8b6,#c2ad7c);text-align:center}
.featured h2{font:500 18px Cabin,sans-serif;color:#333;text-align:left;padding:18px 0 0 46px;height:46px;border-bottom:1px solid #cdbf98}
.feat-icon{position:absolute;left:12px;top:10px}
.featured h3{font:600 13.5px Cabin,sans-serif;color:var(--rust);margin-top:17px}
.featured .thumb{width:160px;height:106px;margin:9px auto 0;border:2px solid #fff}
.featured p{font-size:12px;line-height:16px;color:#222;margin:13px 14px 0}
.details{display:inline-block;margin-top:10px;width:166px;height:29px;border-radius:6px;background:linear-gradient(#d8caa2,#b9a577);font:500 14px Cabin,sans-serif;color:#333;line-height:29px;box-shadow:inset 0 0 0 1px #a8966a}
.slider{left:362px;top:210px;width:622px;height:325px;background:#fff;padding:4px}
.slide{width:614px;height:317px;background:linear-gradient(180deg,#9fc3e4 0%,#c9d9e6 35%,#b3a08a 70%,#4e4a3a 100%);position:relative}
.caption{position:absolute;left:18px;bottom:10px;font:400 18px Cabin,sans-serif;color:#fff}
.dots{position:absolute;right:67px;bottom:14px;display:flex;gap:8px}
.dots i{width:11px;height:11px;border-radius:50%;background:#fff}
.dots i.on{background:#b9a577}

/* panels */
.panel{border:1px solid #e7e7e7;box-shadow:0 0 3px rgba(0,0,0,.08);background:#fff}
.panel-head{height:33px;background:linear-gradient(#f7f2de,#d5c48e);font:500 18px Cabin,sans-serif;color:#222;padding:6px 0 0 24px;border-bottom:1px solid #c4b27a}
.upcoming{left:90px;top:574px;width:264px;height:264px}
.item{display:flex;gap:6px;padding:9px 6px 6px 10px;border-bottom:1px solid #e4e4e4;margin:0 4px}
.item:last-child{border-bottom:0}
.item .thumb{flex:none;width:84px;height:55px;background:linear-gradient(#8db4d8,#b8a98e 60%,#3d5a3a)}
.item h4{font:italic 500 11px Cabin,sans-serif;color:var(--gold-text)}
.item p{font-size:11px;line-height:14.5px;color:#222}

.welcome{left:372px;top:580px;width:617px;border-bottom:1px dashed #ccc;padding-bottom:5px;font:400 20px Cabin,sans-serif;color:var(--ink)}
.welcome span{color:var(--gold-text)}
.intro{left:375px;top:621px;width:317px;font-size:11.5px;line-height:16.3px;text-align:justify;color:#222}
.intro p+p{margin-top:16px}
.video{left:707px;top:624px;width:285px;height:186px;background:#111;padding:6px}
.video .frame{height:158px;background:linear-gradient(135deg,#5a6a7a,#b9a89a 50%,#7a3a30);position:relative}
.play{position:absolute;left:117px;top:58px}
.vbar{height:12px;margin-top:3px;display:flex;align-items:center;gap:5px;color:#ccc;font-size:6px}
.vbar .track{flex:1;height:3px;background:#555}
.vbar .track b{display:block;width:22%;height:3px;background:#c33}

.testimonials{left:90px;top:862px;width:264px;height:203px}
.testi{display:flex;gap:12px;padding:12px 0 0 14px;height:80px}
.testi .thumb{flex:none;width:62px;height:55px;background:linear-gradient(#9ec0d8,#c9c4b6 55%,#3a4a2e)}
.testi h4{font:italic 500 11px Cabin,sans-serif;color:var(--gold-text);margin-bottom:3px}
.testi p{font-size:11px;line-height:14.5px;color:#222}
.testi b{font-size:10px;margin-left:18px}

.card{top:862px;height:205px}
.card-head{height:32px;background:linear-gradient(#5a5a5a,#111);color:#fff;font:600 17px Cabin,sans-serif;text-align:center;line-height:32px}
.card .pic{height:105px;margin:6px 11px 0}
.card p{font-size:11px;line-height:16px;color:#222;margin:6px 14px 0}
.card b{display:block;font-size:11px;margin:5px 14px 0}
.buyers{left:387px;width:282px}
.sellers{left:698px;width:293px}
.buyers .pic{background:linear-gradient(#6d9ed0,#c7b689 60%,#8a7a58)}
.sellers .pic{background:linear-gradient(#c8d6e2,#e0d6c8 50%,#c23a30)}

/* footer */
.footer{left:0;top:1107px;width:1083px;height:93px;background:#1e1e1e;color:#eee}
.footnav{left:101px;top:20px;font:400 12.5px Cabin,sans-serif;color:#eee;word-spacing:2px}
.footnav span{margin:0 8px;color:#bbb}
.copy{left:101px;top:44px;font:400 10.5px Cabin,sans-serif;color:#ddd}
.contact{left:101px;top:65px;font-size:11px;color:#ddd}
.badges{left:745px;top:0;width:243px;height:93px;background:#0c0c0c;display:flex;align-items:center;justify-content:space-around;padding:0 12px}
</style>
</head>
<body>
<div class="abs topline"></div>
<header class="abs header"></header>
<div class="abs brand">Harborline<small>Auction Realty</small></div>
<div class="abs mailer-label">Brightway Mailer</div>
<div class="abs mailer-input">Enter your email address</div>
<div class="abs join">Join Now</div>
<div class="abs follow">Follow us on:</div>
<div class="abs social" aria-label="Social links"><span></span><span></span><span></span><span></span></div>
<div class="abs phone">
  <svg width="22" height="22" viewBox="0 0 22 22"><rect width="22" height="22" rx="3" fill="#3a4048"/><path d="M7 5c-1 1-1.5 2-1 4 1 3 4 7 8 8 2 .5 3 0 4-1l-2-3-2 1c-2-1-3-3-4-5l1-2z" fill="#fff"/></svg>
  +1 (555) 318 0142
</div>

<nav class="abs nav">
  <a style="width:196px">HOME</a><a style="width:123px">ABOUT US</a><a style="width:145px">AUCTIONS</a><a style="width:127px">BUYERS</a><a style="width:146px">SELLERS</a><a style="width:135px">MEDIA</a><a style="width:211px">CONTACT US</a>
</nav>

<section class="abs hero"></section>
<div class="abs dropdown"><div>Upcoming</div><div class="on">Online</div><div>Past</div></div>

<aside class="abs featured">
  <svg class="feat-icon" width="28" height="28" viewBox="0 0 28 28"><path d="M3 14 14 4l11 10" fill="none" stroke="#b0501a" stroke-width="2.5"/><rect x="7" y="13" width="14" height="12" fill="none" stroke="#7a5a3a" stroke-width="2"/><rect x="12" y="17" width="4" height="8" fill="#7a5a3a"/></svg>
  <h2>FEATURED AUCTIONS</h2>
  <h3>Single Family Home Auction</h3>
  <div class="thumb photo" role="img" aria-label="Modern single family home with pool at dusk" style="background:linear-gradient(#a9c6e0,#d8d4c8 50%,#3b5a2a)"></div>
  <p>Original Price: $6.1M - Sealed Bid Auction, Jan. 7th - Published Reserve $3.8 M</p>
  <div class="details">Click here for details &nbsp;»</div>
</aside>

<div class="abs slider">
  <div class="slide photo" role="img" aria-label="Large suburban house at dusk with an auction sign on the lawn">
    <div class="caption">Lorem ipsum dolor sit amet,</div>
    <div class="dots"><i></i><i class="on"></i><i></i><i></i><i></i></div>
  </div>
</div>

<section class="abs panel upcoming">
  <div class="panel-head">Upcoming &nbsp;Auctions</div>
  <div class="item"><div class="thumb photo" role="img" aria-label="Home listing photo"></div><div><h4>Single Family Home Auction</h4><p>Original Price: $6.1M - Sealed Bid Auction, Jan. 7th - Published Reserve $3.8 M</p></div></div>
  <div class="item"><div class="thumb photo" role="img" aria-label="Home listing photo"></div><div><h4>Single Family Home Auction</h4><p>Original Price: $6.1M - Sealed Bid Auction, Jan. 7th - Published Reserve $3.8 M</p></div></div>
  <div class="item"><div class="thumb photo" role="img" aria-label="Home listing photo"></div><div><h4>Single Family Home Auction</h4><p>Original Price: $6.1M - Sealed Bid Auction, Jan. 7th - Published Reserve $3.8 M</p></div></div>
</section>

<h1 class="abs welcome">WELCOME TO <span>HARBORLINE AUCTION REALTY</span></h1>
<div class="abs intro">
  <p>We would like to say a big Thankyou.We would like to say a big Thankyou.We would like to say a big Thankyou.We would like to say a big Thankyou.We would like to say a big Thankyou.We would like to say a big Thankyou.We would like to say a big Thankyou.We</p>
  <p>would like to say a big Thankyou.We would like to say a big Thankyou.We would like to say a big Thankyou.We would like to say a big Thankyou.We would like to say a big Thankyou.We would like to say a big Thankyou.We would like to say a big Thankyou.</p>
</div>
<div class="abs video">
  <div class="frame photo" role="img" aria-label="Video still of a couple reviewing papers with an agent">
    <svg class="play" width="46" height="46" viewBox="0 0 46 46"><circle cx="23" cy="23" r="23" fill="rgba(40,40,40,.6)"/><path d="M17 13v20l16-10z" fill="#ddd"/></svg>
  </div>
  <div class="vbar"><svg width="8" height="8"><path d="M1 0v8l7-4z" fill="#ccc"/></svg><div class="track"><b></b></div><span>00:01 / 10:01</span></div>
</div>

<section class="abs panel testimonials">
  <div class="panel-head" style="padding-left:38px">Clients Testimonials</div>
  <div class="testi"><div class="thumb photo" role="img" aria-label="Client standing in front of a house"></div><div><h4>Mr &amp; Mrs Dalton Reyes WA</h4><p>We would like to say a big Thankyou.<br>The renovations .... <b>Read more</b></p></div></div>
  <div class="testi"><div class="thumb photo" role="img" aria-label="Client standing in front of a house"></div><div><h4>Mr &amp; Mrs Dalton Reyes WA</h4><p>We would like to say a big Thankyou.<br>The renovations .... <b>Read more</b></p></div></div>
</section>

<section class="abs panel card buyers">
  <div class="card-head">BUYERS</div>
  <div class="pic photo" role="img" aria-label="Buyer holding a folder in front of a new home"></div>
  <p>We would like to say a big Thankyou.We would like to say a big Thankyou.</p>
  <b>Read more...</b>
</section>
<section class="abs panel card sellers">
  <div class="card-head">SELLERS</div>
  <div class="pic photo" role="img" aria-label="Seller holding keys beside a for sale sign"></div>
  <p>We would like to say a big Thankyou.We would like to say a big Thankyou.</p>
  <b>Read more...</b>
</section>

<footer class="abs footer">
  <div class="abs footnav">Home<span>\</span>Auctions<span>\</span>About Us<span>\</span>Buyers<span>\</span>Sellers<span>\</span>Media<span>\</span>Contact Us.</div>
  <div class="abs copy">Copyright © 2007 - 2013 - HarborlineAuction.example - All Rights Reserved.</div>
  <div class="abs contact">Toll-Free: (555) 864-0160 , &nbsp;Email: harborlineauction.example</div>
  <div class="abs badges" aria-label="Association memberships">
    <svg width="56" height="70"><rect x="2" y="8" width="52" height="54" rx="26" fill="#bbb"/></svg>
    <svg width="50" height="70"><rect x="4" y="6" width="42" height="58" fill="#ddd"/></svg>
    <svg width="50" height="70"><rect x="4" y="6" width="42" height="58" fill="#eee"/></svg>
  </div>
</footer>
</body>
</html>
```